Introduction of new dentist and new treatments

We want inform our Patients of our new dentist and new treatment methods. It is dealing about biologic dentistry and holistic dentistry. we are in switzerland and speak german

Font styles to use
Sans Serif

Colors
00a990
33b8a4
9bcb3c
acd036
cadf82
0292cd
3176b5
e34297
e667a6

Requirements
Must have
• Text, which can be edited. It will be in german
• Name of the dental clinic is
• "Brivana - Ihr Zahnarzt in Zug"
Nice to have
• A4 Layout

```html
<!DOCTYPE html>
<html lang="de">
<head>
<meta charset="utf-8">
<title>Brivana - Ihr Zahnarzt in Zug</title>
<link href="https://fonts.googleapis.com/css2?family=Lato:wght@400;700&family=Oswald:wght@600&display=swap" rel="stylesheet">
<style>
  :root {
    --canvas: #e9ebec;
    --paper: #f3f5f6;
    --paper-grey: #e4e8ea;
    --brand-blue: #0292cd;
    --green: #2e8b37;
    --green-light: #4a9e50;
    --green-panel: rgba(255,255,255,0.18);
    --ink: #2b2f33;
    --ink-soft: #4a4f54;
    --white: #ffffff;
  }
  * { box-sizing: border-box; margin: 0; padding: 0; }
  html, body { width: 1120px; height: 1200px; overflow: hidden; background: var(--canvas); }
  .flyer {
    position: absolute; left: 150px; top: 30px;
    width: 820px; height: 1140px;
    background: var(--paper);
    font-family: "Lato", sans-serif;
    overflow: hidden;
    box-shadow: 0 2px 10px rgba(0,0,0,0.12);
  }
  .brand { position: absolute; left: 30px; top: 150px; color: var(--brand-blue); }
  .brand-name { font-size: 58px; font-weight: 700; line-height: 1; letter-spacing: 0.5px; }
  .brand-tagline { font-size: 28px; font-weight: 700; margin-top: 8px; margin-left: 4px; }
  .hero-photo {
    position: absolute; left: 300px; top: 0; width: 520px; height: 520px;
    background: radial-gradient(ellipse at 60% 40%, #d9b9a3 0%, #b88f78 35%, #7b5a4a 65%, #d7dcdf 100%);
  }
  .wave { position: absolute; left: 0; top: 270px; width: 820px; height: 260px; }
  .green-body { position: absolute; left: 0; top: 520px; width: 820px; height: 370px; background: var(--green); }
  .headline {
    position: absolute; left: 37px; top: 370px;
    font-family: "Oswald", sans-serif; font-weight: 600;
    font-size: 24px; line-height: 32px; color: var(--white);
  }
  .intro {
    position: absolute; left: 35px; top: 538px; width: 745px;
    background: var(--green-panel); color: var(--white);
    font-size: 15px; line-height: 19px; text-align: center; padding: 8px 24px;
  }
  .column { position: absolute; top: 622px; width: 360px; color: var(--white); }
  .column.left { left: 33px; }
  .column.right { left: 420px; top: 634px; }
  .column h2 { font-size: 21px; font-weight: 700; line-height: 23px; margin-bottom: 12px; }
  .column p { font-size: 13px; line-height: 16.5px; }
  .info { position: absolute; left: 0; top: 890px; width: 820px; height: 250px; background: var(--paper-grey); padding: 20px 40px 0 45px; color: var(--ink); }
  .info h2 { font-size: 20px; font-weight: 700; margin-bottom: 10px; }
  .info p { font-size: 13px; line-height: 15.5px; color: var(--ink-soft); margin-bottom: 14px; }
</style>
</head>
<body>
<main class="flyer">
  <div class="hero-photo" role="img" aria-label="Foto: lächelnde Patientin bei der zahnärztlichen Untersuchung"></div>

  <div class="brand">
    <div class="brand-name">Brivana</div>
    <div class="brand-tagline">Ihr Zahnarzt in Zug</div>
  </div>

  <svg class="wave" viewBox="0 0 820 260" preserveAspectRatio="none" aria-hidden="true">
    <path d="M0,45 C110,5 240,-5 380,40 C520,90 600,220 720,200 C770,192 800,170 820,140 L820,260 L0,260 Z" fill="#ffffff"/>
    <path d="M0,65 C110,25 240,18 380,62 C520,108 600,245 720,222 C770,214 800,192 820,162 L820,260 L0,260 Z" fill="var(--green)"/>
  </svg>
  <div class="green-body"></div>

  <h1 class="headline">Interdisziplinäre Zahnmedizin<br>Zusammenhang zwischen<br>Zahnproblemen und der Gesundheit<br>von Körper und Geist</h1>

  <p class="intro">Zahn und Gesundheit haben eins gemeinsam – Man vermisst sie, wenn sie fehlt. Zähne haben einen engen Zusammenhang zur Gesundheit und können diese beeinflussen. Sowohl negativ als auch positiv.</p>

  <section class="column left">
    <h2>Funktion des Kauorgans und interdisziplinäre Zahnmedizin</h2>
    <p>„Funktion ist nicht alles. Aber ohne Funktion ist alles nichts!“ Sagte einst Prof. A. Lindner (Zahnarzt, Gnathologie) und betonte die Bedeutung der Funktion des Kausystems. Sprechen, Kauen aber auch Körperhaltung und Stressmanagement gehören zu den Funktionen der Zähne. Ein gut funktionierendes Kauorgan (nach Prof. R. Varga, interdisziplinäre Zahnmedizin) kann Stress bewältigen und mehr Leistung und Wohlbefinden bringen. Sehr oft erkennt man Funktionsstörungen daran, dass die Zähne nicht richtig zueinander passen oder Muskelverspannungen und Schmerzen im Kiefergelenk auftreten.</p>
  </section>

  <section class="column right">
    <h2>Parodontitis und systemische Erkrankungen</h2>
    <p>Parodontitis (Entzündung des Zahnhalteapparats) ist eine der häufigsten chronischen Krankheiten weltweit und daher gut erforscht. Herzkrankheiten, Diabetes und Frühgeburtlichkeit sind einige der systemischen Krankheiten mit der Parodontitis in Zusammenhang steht. Zahnfleischbluten, Zahnlockerung, Zahnfleischschwund und Zahnverlust sind typische Begleiterscheinungen von Parodontitis. Eine systematische Parodontitis-Behandlung kann auch positive Auswirkungen auf die gesamte Gesundheit haben.</p>
  </section>

  <section class="info">
    <h2>Zahnverlust und neurologische Auswirkung</h2>
    <p>Ein physiologisches Kausystem hat sehr feine Steuerungs- und Wahrnehmungsmöglichkeiten. Bei Zahnverlust werden diese Fähigkeiten weniger benötigt. Weniger gebrauchte Ressourcen werden von der Natur dementsprechend abgebaut. Studien zeigen, dass Menschen mit weniger Zähnen mehr Risiko zur Bildung von Demenz bergen.</p>
    <h2>Ganzheitliche Erklärungen</h2>
    <p>Die komplementäre Zahnheilkunde, sehr oft auch als ganzheitliche oder biologische Zahnheilkunde bezeichnet, versucht mit Hilfe von Meridianen (Traditionelle Chinesische Medizin), den Zusammenhang zwischen Zähnen und anderen Organen und Körperteilen zu erklären. Es gibt immer mehr Patienten und Zahnärzte die von dieser Theorie und deren Ergebnissen überzeugt sind. Aufgrund der wissenschaftlichen Lage ist eine ausführliche Aufklärung vor der Behandlung sehr ratsam.</p>
  </section>
</main>
</body>
</html>
```